Redesign projects page on UK roofing website

Hi guys,

We would like to redesign the projects page of our roofing company website; https://www.brindleroofing.com/projects

We would like to keep the top of the page the same (up to the big image). Also the footer design should remain the same.

We would like to have some nice photos of work we have done with a little bit of writing about each project.

This site has a nice projects page layout; https://www.wtpbld.com/projects

Something along those lines would work well for our needs.

Thanks

```html
<!DOCTYPE html>
<html lang="en">
<head>
<meta charset="utf-8">
<title>Projects | Brindle Roofing</title>
<link rel="stylesheet" href="https://fonts.googleapis.com/css2?family=Outfit:wght@300;400;500;600;700&display=swap">
<style>
:root{
  --navy:#0d4277;
  --card:#0c4a86;
  --accent:#1aa7df;
  --pale:#f2f5f8;
  --ink:#1d2a38;
  --white:#ffffff;
}
*{margin:0;padding:0;box-sizing:border-box}
html,body{width:1200px;height:2213px;overflow:hidden}
body{font-family:"Outfit",sans-serif;color:var(--ink);background:var(--white);position:relative}
a{color:inherit;text-decoration:none}

/* hero */
.hero{position:absolute;left:0;top:0;width:1200px;height:547px;overflow:hidden}
.hero-photo{position:absolute;inset:0;background:linear-gradient(175deg,#2c2c2c 0%,#5a5a5a 45%,#4a4a4a 75%,#2e2e2e 100%)}
.brand{position:absolute;display:flex;align-items:center;gap:7px;font-weight:600;color:var(--white);letter-spacing:-.5px}
.brand-dot{border-radius:50%;background:var(--white)}
.hero .brand{left:230px;top:15px;font-size:24px}
.hero .brand-dot{width:22px;height:22px}
.nav{position:absolute;top:21px;left:480px;font-size:10px;color:var(--white)}
.nav a{position:absolute;white-space:nowrap}
.nav a.current::after{content:"";position:absolute;left:0;right:0;top:15px;height:2px;background:var(--accent)}
.btn-quote{position:absolute;background:var(--accent);color:var(--white);font-size:10px;font-weight:600;display:flex;align-items:center;justify-content:center}
.hero .btn-quote{left:857px;top:15px;width:113px;height:28px}
.hero-title{position:absolute;left:230px;top:218px;font-size:48px;line-height:55px;font-weight:700;color:var(--white);letter-spacing:-.5px}
.hero-title em{font-style:normal;color:var(--accent)}
.hero-aside{position:absolute;left:785px;top:183px;height:179px;border-left:2px solid var(--accent);padding-left:16px;color:var(--white);width:148px}
.hero-aside h2{font-size:22px;line-height:27px;font-weight:600;margin-top:12px}
.hero-aside p{font-size:12px;line-height:19px;font-weight:300;margin-top:11px}

/* body area */
.backdrop{position:absolute;left:615px;top:540px;width:1100px;height:1100px;border-radius:50%;background:var(--pale)}
.filters{position:absolute;left:233px;top:584px;display:flex;gap:13px}
.filter{height:36px;border:1px solid var(--accent);background:var(--white);color:var(--accent);display:flex;align-items:center;gap:6px;padding:0 18px;font-size:11px;font-weight:500}
.filter.active{background:var(--accent);color:var(--white)}
.filter-icon{width:24px;height:24px;border-radius:50%;background:var(--accent)}
.filter.active .filter-icon{background:var(--white)}
.section-title{position:absolute;left:233px;top:651px;font-size:24px;font-weight:600;color:var(--navy)}
.section-intro{position:absolute;left:233px;top:698px;width:482px;font-size:9.6px;line-height:14px;color:#2a2f36}

.grid{position:absolute;left:233px;top:783px;display:grid;grid-template-columns:236px 236px 236px;column-gap:13px;row-gap:25px}
.project{height:311px;background:var(--card);color:var(--white);position:relative;overflow:hidden}
.project-photo{height:188px}
.project-body{padding:12px 12px}
.project h3{font-size:17px;line-height:20px;font-weight:600}
.project .meta{margin-top:13px;font-size:9.5px;line-height:14px;font-weight:300}
.project.open{background:#2f6398}
.project.open .project-body{padding:26px 12px}
.project.open h4{font-size:9.5px;font-weight:600;margin-top:14px}
.project.open p{font-size:9.5px;line-height:13.7px;font-weight:300}
.project.open .more{display:flex;align-items:center;gap:8px;font-size:9.5px;font-weight:600;margin-top:13px}

.photo-sky{background:linear-gradient(180deg,#c9ced4 0%,#9aa2ab 45%,#4b5158 70%,#2f3338 100%)}
.photo-garden{background:linear-gradient(180deg,#b9c2c9 0%,#6b7560 40%,#a4adb5 65%,#cfd5da 100%)}
.photo-sheet{background:linear-gradient(180deg,#c7ccd1 0%,#9fa6ad 45%,#3d3f42 60%,#2f3134 100%)}
.photo-aerial{background:linear-gradient(180deg,#8c8f7c 0%,#a4adb6 35%,#c9d1d8 65%,#7c868f 100%)}
.photo-cladding{background:linear-gradient(180deg,#9aa0a6 0%,#cfd4d8 45%,#b5bbc1 75%,#7b8189 100%)}
.photo-glazing{background:linear-gradient(180deg,#d5d8db 0%,#9da3a8 45%,#7d8389 75%,#5b6b80 100%)}
.photo-blue{background:linear-gradient(180deg,#8fb3dd 0%,#c7d6e6 25%,#3f5f8e 40%,#6d737a 60%,#3b3f44 100%)}

.pager{position:absolute;left:494px;top:1799px;display:flex;align-items:center;gap:14px;font-size:10px}
.pager .prev{color:#b9c3cf;display:flex;align-items:center;gap:10px}
.pager .next{color:var(--navy);display:flex;align-items:center;gap:10px;margin-left:8px}

/* review strip */
.review-strip{position:absolute;left:3px;top:1877px;width:1194px;height:50px;background:var(--pale)}
.rating{position:absolute;left:245px;top:1893px;display:flex;align-items:center;gap:10px;font-size:11px;color:#333}
.rating-boxes{display:flex;gap:2px}
.rating-boxes span{width:12px;height:12px;background:var(--accent)}
.rating small{font-size:8px}
.review-strip-btn{left:855px;top:1885px;width:112px;height:29px}

/* footer */
.footer{position:absolute;left:0;top:1927px;width:1200px;height:286px;background:var(--navy);color:var(--white)}
.foot-col{position:absolute;top:38px}
.foot-col h5{font-size:12.5px;font-weight:600;margin-bottom:10px}
.foot-col ul{list-style:none}
.foot-col li{font-size:8.5px;font-weight:300;height:26px}
.foot-col .follow{margin-top:22px}
.foot-col .social{display:flex;align-items:center;gap:6px}
.foot-col .social i{width:9px;height:9px;background:var(--white);display:inline-block}
.footer .brand{left:669px;top:43px;font-size:24px}
.footer .brand-dot{width:22px;height:22px}
.legal-note{position:absolute;left:669px;top:78px;width:290px;font-size:8px;line-height:10px;font-weight:300}
.legal-note p{margin-bottom:6px}
.badges{position:absolute;left:669px;top:139px;display:flex;gap:16px;align-items:center}
.badges span{background:rgba(255,255,255,.85);display:block}
.rule{position:absolute;left:233px;top:245px;width:733px;height:1px;background:rgba(255,255,255,.2)}
.copyright{position:absolute;left:233px;top:260px;font-size:8px;font-weight:300}
</style>
</head>
<body>

<header class="hero">
  <div class="hero-photo" role="img" aria-label="Black and white photo of a steel factory roof"></div>
  <a class="brand" href="#"><span class="brand-dot"></span>brindleroofing</a>
  <nav class="nav">
    <a style="left:0" href="#">Services</a>
    <a style="left:79px" href="#">Clients</a>
    <a style="left:152px" class="current" href="#">Projects</a>
    <a style="left:230px" href="#">Team</a>
    <a style="left:297px" href="#">Contact</a>
  </nav>
  <a class="btn-quote" href="#">Get a quote</a>
  <h1 class="hero-title">Some of our <em>latest</em><br><em>projects.</em></h1>
  <div class="hero-aside">
    <h2>What we're working on</h2>
    <p>Keep an eye on some of the latest installs, refurbs and repairs we've carried out.</p>
  </div>
</header>

<div class="backdrop"></div>

<div class="filters">
  <a class="filter active" href="#" style="width:81px"><span class="filter-icon"></span>All</a>
  <a class="filter" href="#" style="width:119px"><span class="filter-icon"></span>Single Ply</a>
  <a class="filter" href="#" style="width:141px"><span class="filter-icon"></span>Liquid Roofing</a>
  <a class="filter" href="#" style="width:137px"><span class="filter-icon"></span>Steel Roofing</a>
  <a class="filter" href="#" style="width:110px"><span class="filter-icon"></span>Asphalt</a>
</div>

<h2 class="section-title">All Projects</h2>
<p class="section-intro">Single ply is one of the most popular flat roofing materials in today's market due to its lightweight and durable design. Single Ply is commonly used on large commercial buildings such as Hospitals, Schools and Universities thanks to the speed at which it can be installed. We install a variety of single ply systems including Vantex-Ply, Duraseal Shieldplan and Corvel Flex systems.</p>

<main class="grid">
  <article class="project">
    <div class="project-photo photo-sky" role="img" aria-label="Wet single ply flat roof with ductwork under a cloudy sky"></div>
    <div class="project-body">
      <h3>University of Northmoor, Colchester</h3>
      <p class="meta">Type: Single-ply (Shieldplan)<br>Roof Size: 2300m2<br>Date of Completion: September, 2020</p>
    </div>
  </article>
  <article class="project open">
    <div class="project-body">
      <h3>Hallow Vale District Council, Uxbridge</h3>
      <p class="meta">Type: Single-ply (Vantex-Ply S)<br>Roof Size: 300m2<br>Date of Completion: March, 2020</p>
      <h4>Contract Description</h4>
      <p>The client approached Brindle to carry out a survey of their existing flat roof coverings which were leaking in numerous places. Upon inspection our engineers quickly discovered the roofs were at end of life and required replacement. Brindle replaced all of the roofs with a new Vantex-Ply single ply membrane with a 20 year manufacturer backed warranty.</p>
      <a class="more" href="#">Get In Touch Know More
        <svg width="22" height="8" viewBox="0 0 22 8"><path d="M0 4h20M16 1l4 3-4 3" fill="none" stroke="#fff" stroke-width="1"/></svg></a>
    </div>
  </article>
  <article class="project">
    <div class="project-photo photo-garden" role="img" aria-label="Pale grey flat roof beside houses and trees"></div>
    <div class="project-body">
      <h3>Private, Watford</h3>
      <p class="meta">Type: Single-ply (Vantex-Ply S)<br>Roof Size: 120m2<br>Date of Completion: February, 2020</p>
    </div>
  </article>

  <article class="project">
    <div class="project-photo photo-sheet" role="img" aria-label="Insulated composite roof panels above a dark flat roof"></div>
    <div class="project-body">
      <h3>Saffron Leaf Kitchens, Billericay</h3>
      <p class="meta">Type: Insulated Composite Panels<br>Roof Size: 900m2<br>Date of Completion: January, 2021</p>
    </div>
  </article>
  <article class="project">
    <div class="project-photo photo-aerial" role="img" aria-label="Aerial view of long overclad industrial roofs with rooflights"></div>
    <div class="project-body">
      <h3>Carrow Lane, Barking</h3>
      <p class="meta">Type: Single Skin Overclad<br>Roof Size: 2200m2<br>Date of Completion: Octobar, 2020</p>
    </div>
  </article>
  <article class="project">
    <div class="project-photo photo-cladding" role="img" aria-label="Pale steel cladding roof with brick chimneys"></div>
    <div class="project-body">
      <h3>Toolhaus, Finchley</h3>
      <p class="meta">Type: Double Skin Steel Cladding<br>Roof Size: 450m2<br>Date of Completion: March, 2020</p>
    </div>
  </article>

  <article class="project">
    <div class="project-photo photo-glazing" role="img" aria-label="Glazed walkway roof over a hospital courtyard"></div>
    <div class="project-body">
      <h3>Wren Hospital, Beckton</h3>
      <p class="meta">Type: Liquid Waterproofing (Coatrex 770)<br>Roof Size: 70m2<br>Date of Completion: March, 2020</p>
    </div>
  </article>
  <article class="project">
    <div class="project-photo photo-blue" role="img" aria-label="Newly overclad grey steel roof under blue sky"></div>
    <div class="project-body">
      <h3>Foresight Works Ltd, Hemel Hempstead</h3>
      <p class="meta">Type: Single Skin Overclad<br>Roof Size: 475m2<br>Date of Completion: March, 2020</p>
    </div>
  </article>
  <article class="project">
    <div class="project-photo photo-blue" role="img" aria-label="Grey steel roof sheets under blue sky"></div>
    <div class="project-body">
      <h3>Private, Watford</h3>
      <p class="meta">Type: Single-ply (Vantex-Ply S)<br>Roof Size: 120m2<br>Date of Completion: February, 2020</p>
    </div>
  </article>
</main>

<nav class="pager">
  <a class="prev" href="#"><svg width="22" height="8" viewBox="0 0 22 8"><path d="M22 4H2M6 1L2 4l4 3" fill="none" stroke="#b9c3cf" stroke-width="1"/></svg>Previous Project</a>
  <a class="next" href="#">Next Project<svg width="22" height="8" viewBox="0 0 22 8"><path d="M0 4h20M16 1l4 3-4 3" fill="none" stroke="#0d4277" stroke-width="1"/></svg></a>
</nav>

<div class="review-strip"></div>
<div class="rating">Excellent
  <span class="rating-boxes"><span></span><span></span><span></span><span></span><span></span></span>
  <small>39 reviews on ReviewMark</small>
</div>
<a class="btn-quote review-strip-btn" href="#">Get a quote</a>

<footer class="footer">
  <div class="foot-col" style="left:233px">
    <h5>Overview</h5>
    <ul><li>Services</li><li>Clients</li><li>Projects</li><li>Team</li><li>Contact</li></ul>
  </div>
  <div class="foot-col" style="left:356px">
    <h5>Services</h5>
    <ul><li>Asbestos roof removal</li><li>Steel cladding</li><li>Liquid waterproofing</li><li>Mastic asphalt roofing</li><li>Single ply roofing</li><li>Roof repairs</li><li>Emergency roof repairs</li></ul>
  </div>
  <div class="foot-col" style="left:485px">
    <h5>Legal</h5>
    <ul><li>Terms of service</li></ul>
    <h5 class="follow">Follow us</h5>
    <ul><li class="social"><i></i>Profile</li><li class="social"><i></i>Gallery</li></ul>
  </div>
  <a class="brand" href="#"><span class="brand-dot"></span>brindleroofing</a>
  <div class="legal-note">
    <p>Brindle Roofing Ltd is registered in England as a private limited company.</p>
    <p>Registration No: 08472915</p>
    <p>Registered Office: Unit 14 Ashgrove Farm, Mill Lane, Writtle Green, Chelmsford CM2 9QX</p>
  </div>
  <div class="badges">
    <span style="width:76px;height:24px"></span>
    <span style="width:54px;height:32px;border-radius:4px"></span>
    <span style="width:42px;height:42px;border-radius:50%"></span>
    <span style="width:78px;height:26px"></span>
  </div>
  <div class="rule"></div>
  <p class="copyright">© Copyright Brindle Roofing Ltd 2023 | All rights reserved.</p>
</footer>

</body>
</html>
```